Präsentationsvorlagen für Strahlenschutzkurse
Zielgruppe
Wir bieten Strahlenschutzkurse in der Medizin an. Zielgruppe: Ärztinnen und Ärzte
Stichworte: Erwachsenenbildung, wissenschaftliche Inhalte
Aufgabenstellung
Wir benötigen eine Power-Point Präsentationsvorlage für unsere Kurse.
Auf allen Folien:
*Integration von unserem Logo
*Übernahme unseres bestehenden Farbkonzepts
*Feld für Überschrift
*kleines Textfeld für die Angabe der jeweiligen Quelle
Wir benötigen:
eine Folie nur mit Textfeld (z.B. Aufzählung, kurzer Text)
eine Folie Text mit Bild
eine Folie Bild bzw. Video
eine Folie mit einem wichtigen Lehrinhalt (wichtiger Text) - besondere Vorhebung erwünscht
eine Folie für Anfang bzw. Ende
HEX-CODE:
#4f93fe
#eea62f
#ffffff

```html
<!DOCTYPE html>
<html lang="de">
<head>
<meta charset="utf-8">
<title>Folie nur mit Textfeld</title>
<link href="https://fonts.googleapis.com/css2?family=Carlito:wght@400;700&display=swap" rel="stylesheet">
<style>
  :root {
    --title-blue: #3b5b82;
    --brand-blue: #3d5f8a;
    --text-dark: #111111;
    --footer-grey: #9ca8b6;
    --bg-top: #ffffff;
    --bg-bottom: #e8ebef;
    --white: #ffffff;
  }
  html, body {
    margin: 0;
    padding: 0;
    overflow: hidden;
  }
  body {
    width: 1200px;
    height: 675px;
    font-family: "Carlito", "Calibri", sans-serif;
  }
  .slide {
    position: relative;
    width: 1200px;
    height: 675px;
    overflow: hidden;
    background: linear-gradient(180deg, var(--bg-top) 0%, var(--bg-top) 58%, var(--bg-bottom) 100%);
  }
  .brand-mark {
    position: absolute;
    top: 70px;
    right: 36px;
    display: flex;
    align-items: center;
    gap: 8px;
    color: var(--brand-blue);
    font-size: 17px;
    font-weight: 400;
    letter-spacing: 0.3px;
  }
  .brand-dot {
    width: 12px;
    height: 12px;
    border-radius: 50%;
    background: var(--brand-blue);
  }
  .slide-title {
    position: absolute;
    left: 160px;
    top: 104px;
    margin: 0;
    color: var(--title-blue);
    font-size: 46px;
    font-weight: 400;
    line-height: 1.1;
  }
  .content {
    position: absolute;
    left: 160px;
    top: 184px;
    width: 860px;
    color: var(--text-dark);
    font-size: 26px;
  }
  .intro {
    margin: 0 0 22px;
    line-height: 31px;
  }
  .checklist {
    list-style: none;
    margin: 0;
    padding: 0;
  }
  .checklist li {
    display: flex;
    align-items: center;
    height: 45px;
    line-height: 31px;
  }
  .check-icon {
    width: 20px;
    height: 20px;
    margin-right: 13px;
    flex-shrink: 0;
  }
  .footer {
    position: absolute;
    left: 0;
    bottom: 0;
    width: 1200px;
    height: 111px;
    background: var(--footer-grey);
    color: var(--white);
  }
  .footer-brand {
    position: absolute;
    left: 30px;
    top: 44px;
    display: flex;
    align-items: center;
    gap: 8px;
    font-size: 15px;
    letter-spacing: 0.3px;
  }
  .footer-brand-dot {
    width: 10px;
    height: 10px;
    border-radius: 50%;
    background: var(--white);
  }
  .source-field {
    position: absolute;
    left: 867px;
    top: 50px;
    font-size: 19px;
  }
  .page-number {
    position: absolute;
    left: 1146px;
    top: 51px;
    font-size: 17px;
  }
</style>
</head>
<body>
  <div class="slide">
    <div class="brand-mark">
      <span class="brand-dot"></span>
      <span>Lindqvist &amp; Auer</span>
    </div>

    <h1 class="slide-title">Überschrift Folie nur mit Textfeld</h1>

    <div class="content">
      <p class="intro">Lorem ipsum dolor sit amet, consetetur sadipscing elitr, sed diam nonumy eirmod tempor invidunt ut labore et dolore magna aliquyam erat, sed diam voluptua.</p>
      <ul class="checklist">
        <li><svg class="check-icon" viewBox="0 0 20 20"><path d="M2 11 L7.5 16.5 L18 3" fill="none" stroke="#111" stroke-width="2.4" stroke-linecap="round" stroke-linejoin="round"/></svg>Lorem ipsum dolor sit amet</li>
        <li><svg class="check-icon" viewBox="0 0 20 20"><path d="M2 11 L7.5 16.5 L18 3" fill="none" stroke="#111" stroke-width="2.4" stroke-linecap="round" stroke-linejoin="round"/></svg>consetetur sadipscing elitr,</li>
        <li><svg class="check-icon" viewBox="0 0 20 20"><path d="M2 11 L7.5 16.5 L18 3" fill="none" stroke="#111" stroke-width="2.4" stroke-linecap="round" stroke-linejoin="round"/></svg>sed diam nonumy eirmod tempor invidunt ut</li>
        <li><svg class="check-icon" viewBox="0 0 20 20"><path d="M2 11 L7.5 16.5 L18 3" fill="none" stroke="#111" stroke-width="2.4" stroke-linecap="round" stroke-linejoin="round"/></svg>labore et dolore magna aliquyam erat, sed diam voluptua.</li>
      </ul>
    </div>

    <footer class="footer">
      <div class="footer-brand">
        <span class="footer-brand-dot"></span>
        <span>Dr. Lindqvist &amp; Auer Strahlenschutz</span>
      </div>
      <div class="source-field">Feld Quellangaben</div>
      <div class="page-number">3</div>
    </footer>
  </div>
</body>
</html>
```